Square graphic for social media post

I want to create a 1080 x 1080px all-black image for the quote below that I can share on social media. I want the emphasis to be primarily on the quote, secondarily on the portrait, and third (smallest) on the logo. I want the background on the portrait to be edited so it's transparent and just shows the face of the person on a black background (no brick wall visible).

Graphic color: black
Text color: white
Content: "What we went through is going to make the greatest generation of hoteliers our industry has ever seen." << biggest text
Dorian Welk << smaller text
President, Marrowgate Hotels << smaller text
[image of person - use whichever version looks better to you]
[Add Lodging Ledger logo - whichever looks better to you]

This image needs to be readable when sized down much smaller (400x400?) so want the text and portrait to take up most of the space.

I'd like the output both as PNG and original file (preferably Canva). Thanks!

Target Market(s)

Hotel managers

Industry/Entity Type

Hospitality

Font styles to use
Sans Serif

Colors

Designer to choose colors to be used in the design.

Requirements
Must have
• Needs to focus on the quote and the person quoted (the portrait)

```html
<!DOCTYPE html>
<html lang="en">
<head>
<meta charset="utf-8">
<title>Quote Card – Dorian Welk</title>
<link href="https://fonts.googleapis.com/css2?family=PT+Serif:wght@400;700&display=swap" rel="stylesheet">
<style>
  :root {
    --bg: #000000;
    --quote-text: #dcdcdc;
    --quote-mark: #3b3b3b;
    --name: #e6e6e6;
    --title: #7a7a80;
    --logo: #ffffff;
    --skin: #8a5448;
    --jacket: #0e1a4a;
  }
  html, body {
    margin: 0;
    padding: 0;
    width: 1200px;
    height: 1200px;
    overflow: hidden;
    background: var(--bg);
  }
  .card {
    position: relative;
    width: 1200px;
    height: 1200px;
    background: var(--bg);
    font-family: "PT Serif", Georgia, serif;
    overflow: hidden;
  }
  .portrait {
    position: absolute;
    left: 0;
    top: 0;
    width: 760px;
    height: 1200px;
    background:
      radial-gradient(ellipse 48% 40% at 50% 46%, rgba(138,84,72,0.85) 0%, rgba(90,52,44,0.55) 55%, rgba(0,0,0,0) 100%),
      radial-gradient(ellipse 70% 30% at 55% 100%, rgba(14,26,74,0.9) 0%, rgba(0,0,0,0) 100%),
      var(--bg);
  }
  .quote-mark {
    position: absolute;
    color: var(--quote-mark);
    font-family: "PT Serif", Georgia, serif;
    font-weight: 700;
    font-size: 190px;
    line-height: 1;
  }
  .quote-mark--open { left: 744px; top: 44px; }
  .quote-mark--close { left: 1003px; top: 926px; }
  .quote {
    position: absolute;
    right: 116px;
    top: 142px;
    margin: 0;
    text-align: right;
    color: var(--quote-text);
    font-size: 58px;
    line-height: 70px;
    font-weight: 400;
  }
  .quote span { display: block; }
  .attribution {
    position: absolute;
    left: 774px;
    top: 1000px;
  }
  .attribution__name {
    margin: 0;
    color: var(--name);
    font-weight: 700;
    font-size: 25px;
    line-height: 32px;
  }
  .attribution__title {
    margin: 0;
    color: var(--title);
    font-size: 19px;
    line-height: 20px;
  }
  .brand {
    position: absolute;
    left: 62px;
    top: 1060px;
    display: flex;
    align-items: center;
    gap: 12px;
    color: var(--logo);
    font-family: "PT Serif", Georgia, serif;
    font-weight: 700;
    font-size: 22px;
    letter-spacing: 4px;
    text-transform: uppercase;
  }
  .brand__dot {
    width: 12px;
    height: 12px;
    border-radius: 50%;
    background: var(--logo);
  }
</style>
</head>
<body>
  <main class="card">
    <div class="portrait" role="img" aria-label="Smiling portrait of Dorian Welk in a white open-collar shirt and navy jacket against black"></div>

    <div class="quote-mark quote-mark--open" aria-hidden="true">&ldquo;</div>
    <blockquote class="quote">
      <span>What we</span>
      <span>went</span>
      <span>through is</span>
      <span>going to</span>
      <span>make the</span>
      <span>greatest</span>
      <span>generation</span>
      <span>of hoteliers</span>
      <span>our industry</span>
      <span>has ever</span>
      <span>seen.</span>
    </blockquote>
    <div class="quote-mark quote-mark--close" aria-hidden="true">&rdquo;</div>

    <div class="attribution">
      <p class="attribution__name">Dorian Welk</p>
      <p class="attribution__title">President,<br>Marrowgate Hotels</p>
    </div>

    <div class="brand">
      <span class="brand__dot" aria-hidden="true"></span>
      <span class="brand__name">Lodging Ledger</span>
    </div>
  </main>
</body>
</html>
```